Apply Existing Website Design to Pellmoor-Made Tele-Wellness App (UX/UI Work)

We’re looking for a highly skilled UX/UI designer to translate our existing website design into an intuitive, beautiful mobile app interface for our Pellmoor-developed tele-wellness platform. Hoping this designer will stay onboard with us for future work.

Scope of Work:
    •    Review our existing website design (style, colors, typography, components)
    •    Apply the same visual language to our mobile app screens
    •    Ensure consistent, user-friendly experience across the app
    •    Deliver high-fidelity mockups and design assets (preferably in Figma)
    •    Minimal UX rethinking may be needed to optimize for mobile, but the core brand and design system are already established

What We Provide:
    •    Access to the existing website design (including any style guides or component libraries)
    •    Wireframes or a basic functional map of the app screens
    •    Clear guidelines on branding and user flows

Ideal Candidate:
    •    Strong portfolio of mobile app design, especially healthcare/wellness preferred
    •    Proven experience in adapting web designs for mobile apps
    •    Expertise with Figma or comparable tools
    •    Attention to detail and commitment to brand consistency
    •    Ability to deliver quickly while maintaining quality

Deliverables:
    •    Complete set of high-fidelity, mobile-optimized app screens
    •    Organized design file (Figma preferred) ready for developer handoff
    •    Design assets as needed (icons, images, components)

Timeline:
    •    Estimated 1 week for initial delivery, with room for revisions

```html
<!DOCTYPE html>
<html lang="en">
<head>
<meta charset="utf-8">
<title>Veyla Tele-Wellness App Screens</title>
<link href="https://fonts.googleapis.com/css2?family=Inter:wght@400;500;600;700&family=Tinos:wght@400;700&display=swap" rel="stylesheet">
<style>
:root{
  --peach:#fbcfa5;
  --peach-deep:#f6b98a;
  --ink:#1c1c1c;
  --panel:#3b3b3b;
  --surface:#2f2f2f;
  --card:#454545;
  --nav:#0f0f0f;
  --muted:#9a9a9a;
  --white:#ffffff;
  --star:#f2c200;
}
*{box-sizing:border-box;margin:0;padding:0}
html,body{width:1200px;height:913px;overflow:hidden;background:#fff}
body{position:relative;font-family:'Inter',sans-serif;color:var(--white)}
.screen{position:absolute;width:282px;height:610px;border-radius:26px;overflow:hidden;background:var(--surface)}
.screen--welcome{left:98px;top:180px}
.screen--home{left:451px;top:134px}
.screen--store{left:804px;top:180px}
.abs{position:absolute}
.status{position:absolute;top:9px;left:24px;right:14px;display:flex;justify-content:space-between;align-items:center;font-size:11px;font-weight:600;z-index:3}
.status svg{display:block}
.serif{font-family:'Tinos',serif}

/* welcome */
.welcome-photo{position:absolute;inset:0;background:radial-gradient(ellipse at 20% 10%,#c9d2c2 0,#6f8a55 22%,transparent 42%),radial-gradient(ellipse at 85% 12%,#b9c2b2 0,#56763e 25%,transparent 45%),radial-gradient(ellipse at 30% 70%,#3f7a2a 0,#1f3d16 40%,transparent 70%),linear-gradient(180deg,#3a5a2a 0%,#101a0c 40%,#16240f 70%,#0b0f08 100%)}
.welcome-brand{left:31px;top:165px;font-size:38px;font-weight:700;color:var(--peach);letter-spacing:2px}
.welcome-title{left:31px;top:309px;font-size:22px;line-height:22px;color:var(--white)}
.welcome-copy{left:31px;top:376px;font-size:12.5px;line-height:20px}
.welcome-origin{left:31px;top:450px;font-size:15px;font-weight:600}
.btn-start{left:69px;top:493px;width:143px;height:28px;border-radius:14px;background:var(--peach);color:var(--ink);font-size:10px;font-weight:500;display:flex;align-items:center;justify-content:center;letter-spacing:.3px}
.home-indicator{left:91px;top:600px;width:100px;height:3px;border-radius:2px;background:#9c9c9c}

/* home */
.home-header{left:0;top:0;width:282px;height:118px;background:var(--panel);border-radius:0 0 14px 14px}
.brand-small{left:15px;top:40px;font-size:17px;font-weight:700;color:var(--peach);letter-spacing:1px}
.icon-btn{position:absolute;width:23px;height:23px;border-radius:50%;background:var(--surface);display:flex;align-items:center;justify-content:center}
.avatar{left:17px;top:68px;width:38px;height:38px;border-radius:50%;background:linear-gradient(135deg,#8a6a52,#c9a07c 60%,#e6e0d6)}
.greet{left:73px;top:68px;font-size:19px;font-weight:700}
.greet-sub{left:73px;top:92px;font-size:10.5px;color:#b8b8b8}
.dates{left:13px;top:136px;display:flex;gap:14px}
.date{width:23px;height:42px;border-radius:12px;background:var(--card);display:flex;flex-direction:column;align-items:center;justify-content:center;color:var(--muted);font-size:6px;line-height:8px}
.date b{font-size:11px;line-height:12px;font-weight:500}
.date--active{background:var(--peach);color:var(--ink)}
.date--cut{width:6px;border-radius:12px 0 0 12px}
.search{height:28px;border-radius:14px;background:#434343;display:flex;align-items:center;padding-left:6px;font-size:11px;color:#a7a7a7}
.search .dot{width:15px;height:15px;border-radius:50%;background:var(--surface);display:flex;align-items:center;justify-content:center;margin-right:9px}
.search .divider{position:absolute;right:27px;top:4px;width:1px;height:20px;background:#222}
.section-title{left:24px;font-size:14.5px;font-weight:400}
.task{left:21px;width:240px;height:65px;border-radius:6px;background:var(--peach);color:var(--ink);padding:6px 30px 0 6px}
.task h3{font-size:11.5px;font-weight:600;margin-bottom:2px}
.task p{font-size:9.8px;line-height:12px;color:#4a3a2c}
.task .go{position:absolute;right:6px;top:25px;width:16px;height:16px;border-radius:50%;background:#222;display:flex;align-items:center;justify-content:center}
.notice{left:21px;top:447px;width:240px;height:55px;border-radius:6px;background:var(--card);padding:6px}
.notice h3{font-size:11.5px;font-weight:600;margin-bottom:2px}
.notice p{font-size:9.8px;line-height:12px;color:#8f8f8f}
.tabbar{left:0;top:538px;width:282px;height:72px;background:var(--nav)}
.tab{position:absolute;top:0;width:52px;margin-left:-26px;display:flex;flex-direction:column;align-items:center;font-size:7px;font-weight:600;color:#d8d8d8}
.tab .ic{width:28px;height:28px;margin-top:6px;border-radius:50%;display:flex;align-items:center;justify-content:center}
.tab span{margin-top:5px}
.tab--active{color:var(--peach)}
.tab--active .ic{background:var(--peach)}
.tab--active::before{content:"";position:absolute;top:0;width:28px;height:2px;background:var(--peach);border-radius:1px}

/* store */
.store-header{left:0;top:0;width:282px;height:66px;background:var(--panel);border-radius:0 0 14px 14px}
.store-title{left:0;width:282px;top:38px;text-align:center;font-size:14px;font-weight:700}
.chips{left:16px;top:120px;display:flex;gap:6px;align-items:center;white-space:nowrap}
.chip{height:23px;border-radius:12px;background:var(--card);font-size:8.5px;display:flex;align-items:center;justify-content:center}
.chip--on{background:var(--peach);color:var(--ink)}
.product{width:121px;height:160px;border-radius:8px;background:#3c3c3c}
.product .photo{position:absolute;left:5px;top:5px;width:111px;height:110px;border-radius:5px}
.photo--white{background:radial-gradient(circle at 50% 48%,#b8a24a 0,#8a7a30 30%,#f2f2f2 44%,#fafafa 100%)}
.photo--wood{background:radial-gradient(circle at 50% 48%,#6a4a5a 0,#4a3040 28%,#9a6a40 42%,#efebe6 56%,#f6f4f2 100%)}
.photo--leaf{background:radial-gradient(circle at 45% 50%,#9aa868 0,#6f7a45 35%,#7a5230 60%,#4a3626 100%)}
.product .fav{position:absolute;right:6px;top:10px;width:14px;height:14px;border-radius:50%;background:rgba(255,255,255,.55);display:flex;align-items:center;justify-content:center}
.product .maker{position:absolute;left:3px;top:123px;font-size:7px;font-weight:600;color:var(--peach)}
.product .name{position:absolute;left:3px;top:132px;font-size:8.8px}
.product .price{position:absolute;left:3px;top:143px;font-size:10px;font-weight:700}
.product .rate{position:absolute;right:1px;top:146px;font-size:6px;color:#8a8a8a}
.product .rate i{font-style:normal;color:var(--star);letter-spacing:-.5px}
.product .add{position:absolute;right:6px;top:123px;width:14px;height:14px;border-radius:50%;background:var(--peach);display:flex;align-items:center;justify-content:center}
</style>
</head>
<body>

<!-- Welcome screen -->
<section class="screen screen--welcome">
  <div class="welcome-photo" role="img" aria-label="Close-up photo of white flower buds among green leaves"></div>
  <div class="status"><span>9:41</span>
    <svg width="44" height="9" viewBox="0 0 44 9"><g fill="#fff"><rect x="0" y="6" width="2" height="3"/><rect x="3" y="4" width="2" height="5"/><rect x="6" y="2" width="2" height="7"/><rect x="9" y="0" width="2" height="9"/><path d="M15 3a7 7 0 0 1 9 0l-1 1a5.5 5.5 0 0 0-7 0z M17 5.5a4 4 0 0 1 5 0L19.5 8z"/><rect x="29" y="1" width="14" height="7" rx="1.5"/></g></svg>
  </div>
  <div class="abs welcome-brand">VEYLA</div>
  <h1 class="abs welcome-title serif">Holistic-Doctor led care<br>Pay as you like</h1>
  <p class="abs welcome-copy">Evidence based care with heart<br>tailored only for you<br>Tele-Wellness</p>
  <p class="abs welcome-origin">Developed at Pellmoor</p>
  <div class="abs btn-start">GET STARTED</div>
  <div class="abs home-indicator"></div>
</section>

<!-- Home screen -->
<section class="screen screen--home">
  <div class="abs home-header"></div>
  <div class="status"><span>9:41</span>
    <svg width="48" height="9" viewBox="0 0 48 9"><g fill="#fff"><rect x="0" y="6" width="2" height="3"/><rect x="3" y="4" width="2" height="5"/><rect x="6" y="2" width="2" height="7"/><rect x="9" y="0" width="2" height="9"/><path d="M15 3a7 7 0 0 1 9 0l-1 1a5.5 5.5 0 0 0-7 0z M17 5.5a4 4 0 0 1 5 0L19.5 8z"/><rect x="30" y="1" width="16" height="7" rx="1.5"/></g></svg>
  </div>
  <div class="abs brand-small">VEYLA</div>
  <div class="icon-btn" style="left:241px;top:38px"><svg width="10" height="11" viewBox="0 0 10 11"><path d="M5 0.5a3.3 3.3 0 0 1 3.3 3.3v3l1.2 1.5H0.5l1.2-1.5v-3A3.3 3.3 0 0 1 5 0.5zM3.8 9.3h2.4a1.2 1.2 0 0 1-2.4 0z" fill="#fbcfa5"/></svg></div>
  <div class="abs avatar" role="img" aria-label="Profile photo of the user"></div>
  <h2 class="abs greet serif">Hello, Mira !</h2>
  <p class="abs greet-sub">How are you feeling today?</p>

  <div class="abs dates">
    <div class="date">FRI<b>4</b>JULY</div>
    <div class="date">SAT<b>5</b>JULY</div>
    <div class="date">SUN<b>6</b>JULY</div>
    <div class="date date--active">MON<b>7</b>JULY</div>
    <div class="date">TUE<b>8</b>JULY</div>
    <div class="date">WED<b>9</b>JULY</div>
    <div class="date">THU<b>10</b>JULY</div>
    <div class="date date--cut"></div>
  </div>

  <div class="abs search" style="left:15px;top:195px;width:250px">
    <span class="dot"><svg width="8" height="8" viewBox="0 0 8 8"><circle cx="3.3" cy="3.3" r="2.4" fill="none" stroke="#fbcfa5" stroke-width="1.2"/><path d="M5 5l2.3 2.3" stroke="#fbcfa5" stroke-width="1.2"/></svg></span>
    Search for anything..
    <span class="divider"></span>
    <span class="dot" style="position:absolute;right:5px;margin:0;width:17px;height:17px;background:#1e1e1e"><svg width="6" height="9" viewBox="0 0 6 9"><rect x="1.5" y="0" width="3" height="5.5" rx="1.5" fill="#fff"/><path d="M0.5 4a2.5 2.5 0 0 0 5 0M3 6.5v2" stroke="#fff" fill="none" stroke-width=".8"/></svg></span>
  </div>

  <h2 class="abs section-title" style="top:237px">Things To Do</h2>
  <article class="abs task" style="top:265px">
    <h3>Become a Member</h3>
    <p>Become a Member to save on products recommended by our doctors and enjoy exlusive benefits.</p>
    <span class="go"><svg width="6" height="8" viewBox="0 0 6 8"><path d="M1.5 1l3 3-3 3" stroke="#fff" fill="none" stroke-width="1.2"/></svg></span>
  </article>
  <article class="abs task" style="top:345px">
    <h3>Complete the questionnaire</h3>
    <p>Complete the questionnaite to receive a personalized report on your unique contitution from a doctor.</p>
    <span class="go"><svg width="6" height="8" viewBox="0 0 6 8"><path d="M1.5 1l3 3-3 3" stroke="#fff" fill="none" stroke-width="1.2"/></svg></span>
  </article>

  <h2 class="abs section-title" style="top:417px">Coming Soon</h2>
  <article class="abs notice">
    <h3>Courses section Opening soon</h3>
    <p>We are pround to announce our new courses section. Stay tuned for more updates.</p>
  </article>

  <nav class="abs tabbar">
    <div class="tab tab--active" style="left:38px"><div class="ic"><svg width="14" height="14" viewBox="0 0 14 14"><path d="M7 1l6 5v7H9V9H5v4H1V6z" fill="#111"/></svg></div><span>HOME</span></div>
    <div class="tab" style="left:90px"><div class="ic"><svg width="13" height="14" viewBox="0 0 13 14"><rect x="1" y="2.5" width="11" height="10.5" rx="1" fill="none" stroke="#ddd" stroke-width="1.3"/><path d="M1 5.5h11M4 1v3M9 1v3M4 9l2 2 3-3.5" stroke="#ddd" fill="none" stroke-width="1.3"/></svg></div><span>BOOK</span></div>
    <div class="tab" style="left:142px"><div class="ic"><svg width="14" height="14" viewBox="0 0 14 14"><path d="M1 1h12v9H4l-3 3z" fill="#ddd"/><path d="M3.5 4h7M3.5 6.5h7" stroke="#111" stroke-width="1"/></svg></div><span>CHAT</span></div>
    <div class="tab" style="left:195px"><div class="ic"><svg width="14" height="14" viewBox="0 0 14 14"><path d="M0.5 1h2l2 7.5h7l1.5-5.5H3.5" fill="none" stroke="#ddd" stroke-width="1.3"/><path d="M3.7 3h9.3l-1.5 5.5h-7z" fill="#ddd"/><circle cx="5" cy="12" r="1.2" fill="#ddd"/><circle cx="11" cy="12" r="1.2" fill="#ddd"/></svg></div><span>STORE</span></div>
    <div class="tab" style="left:245px"><div class="ic"><svg width="12" height="13" viewBox="0 0 12 13"><circle cx="6" cy="3.5" r="3" fill="#ddd"/><path d="M0 13c0-4 2.5-5.5 6-5.5S12 9 12 13z" fill="#ddd"/></svg></div><span>PROFILE</span></div>
  </nav>
</section>

<!-- Store screen -->
<section class="screen screen--store">
  <div class="abs store-header"></div>
  <div class="status"><span>9:41</span>
    <svg width="48" height="9" viewBox="0 0 48 9"><g fill="#fff"><rect x="0" y="6" width="2" height="3"/><rect x="3" y="4" width="2" height="5"/><rect x="6" y="2" width="2" height="7"/><rect x="9" y="0" width="2" height="9"/><path d="M15 3a7 7 0 0 1 9 0l-1 1a5.5 5.5 0 0 0-7 0z M17 5.5a4 4 0 0 1 5 0L19.5 8z"/><rect x="30" y="1" width="16" height="7" rx="1.5"/></g></svg>
  </div>
  <div class="icon-btn" style="left:15px;top:38px"><svg width="8" height="9" viewBox="0 0 8 9"><path d="M7 0.5v8L1 4.5z" fill="#fbcfa5"/></svg></div>
  <h1 class="abs store-title serif">Store</h1>
  <div class="icon-btn" style="left:214px;top:38px"><svg width="11" height="10" viewBox="0 0 11 10"><path d="M5.5 9.5L1 5a2.6 2.6 0 0 1 4.5-3.2A2.6 2.6 0 0 1 10 5z" fill="#fbcfa5"/></svg></div>
  <div class="icon-btn" style="left:243px;top:38px"><svg width="11" height="11" viewBox="0 0 14 14"><path d="M0.5 1h2l2 7.5h7l1.5-5.5H3.5" fill="none" stroke="#fbcfa5" stroke-width="1.5"/><path d="M3.7 3h9.3l-1.5 5.5h-7z" fill="#fbcfa5"/><circle cx="5" cy="12" r="1.3" fill="#fbcfa5"/><circle cx="11" cy="12" r="1.3" fill="#fbcfa5"/></svg></div>

  <div class="abs search" style="left:16px;top:81px;width:250px;background:#3f3f3f">
    <span class="dot"><svg width="8" height="8" viewBox="0 0 8 8"><circle cx="3.3" cy="3.3" r="2.4" fill="none" stroke="#fff" stroke-width="1.2"/><path d="M5 5l2.3 2.3" stroke="#fff" stroke-width="1.2"/></svg></span>
    Search for anything..
    <span class="divider" style="right:28px;background:#222"></span>
  </div>

  <div class="abs chips">
    <div class="chip" style="width:18px;border-radius:9px;height:18px"><svg width="9" height="8" viewBox="0 0 9 8"><path d="M0 1.5h9M0 4h9M0 6.5h9" stroke="#ddd" stroke-width=".9"/><circle cx="6" cy="1.5" r="1" fill="#ddd"/><circle cx="3" cy="4" r="1" fill="#ddd"/><circle cx="6" cy="6.5" r="1" fill="#ddd"/></svg></div>
    <div class="chip chip--on" style="width:57px">All</div>
    <div class="chip chip--on" style="width:71px">Bati/Tablet</div>
    <div class="chip" style="width:71px">Churnas</div>
    <div class="chip" style="width:30px"></div>
  </div>

  <article class="abs product" style="left:15px;top:159px">
    <div class="photo photo--white" role="img" aria-label="Dried herbal flowers in a white bowl"></div>
    <span class="fav"><svg width="8" height="7" viewBox="0 0 11 10"><path d="M5.5 9.5L1 5a2.6 2.6 0 0 1 4.5-3.2A2.6 2.6 0 0 1 10 5z" fill="none" stroke="#fff" stroke-width="1.3"/></svg></span>
    <span class="maker">Herbvale</span><span class="add"><svg width="7" height="7" viewBox="0 0 7 7"><path d="M3.5 0.5v6M0.5 3.5h6" stroke="#111" stroke-width="1.2"/></svg></span>
    <span class="name">Mahayograj Guggulu</span><span class="price">$9.99</span>
    <span class="rate">4.0 <i>★★★★★</i> (20)</span>
  </article>
  <article class="abs product" style="left:145px;top:159px">
    <div class="photo photo--wood" role="img" aria-label="Dried rose petals in a wooden bowl"></div>
    <span class="fav"><svg width="8" height="7" viewBox="0 0 11 10"><path d="M5.5 9.5L1 5a2.6 2.6 0 0 1 4.5-3.2A2.6 2.6 0 0 1 10 5z" fill="#fff"/></svg></span>
    <span class="maker">Herbvale</span><span class="add"><svg width="7" height="7" viewBox="0 0 7 7"><path d="M3.5 0.5v6M0.5 3.5h6" stroke="#111" stroke-width="1.2"/></svg></span>
    <span class="name">Arjun Ghanvati</span><span class="price">$9.99</span>
    <span class="rate">4.0 <i>★★★★★</i> (20)</span>
  </article>
  <article class="abs product" style="left:15px;top:335px">
    <div class="photo photo--leaf" role="img" aria-label="Dried leaves and blossoms in a wooden bowl"></div>
    <span class="fav"><svg width="8" height="7" viewBox="0 0 11 10"><path d="M5.5 9.5L1 5a2.6 2.6 0 0 1 4.5-3.2A2.6 2.6 0 0 1 10 5z" fill="none" stroke="#fff" stroke-width="1.3"/></svg></span>
    <span class="maker">Herbvale</span><span class="add"><svg width="7" height="7" viewBox="0 0 7 7"><path d="M3.5 0.5v6M0.5 3.5h6" stroke="#111" stroke-width="1.2"/></svg></span>
    <span class="name">Rasayan Churna</span><span class="price">$9.99</span>
    <span class="rate">4.0 <i>★★★★★</i> (20)</span>
  </article>
  <article class="abs product" style="left:145px;top:335px">
    <div class="photo photo--white" role="img" aria-label="Dried herbal flowers in a white bowl"></div>
    <span class="fav"><svg width="8" height="7" viewBox="0 0 11 10"><path d="M5.5 9.5L1 5a2.6 2.6 0 0 1 4.5-3.2A2.6 2.6 0 0 1 10 5z" fill="none" stroke="#fff" stroke-width="1.3"/></svg></span>
    <span class="maker">Soma Leaf</span><span class="add"><svg width="7" height="7" viewBox="0 0 7 7"><path d="M3.5 0.5v6M0.5 3.5h6" stroke="#111" stroke-width="1.2"/></svg></span>
    <span class="name">Talisadi Churna</span><span class="price">$9.99</span>
    <span class="rate">4.0 <i>★★★★★</i> (20)</span>
  </article>
  <article class="abs product" style="left:15px;top:510px">
    <div class="photo photo--wood" role="img" aria-label="Dried rose petals in a wooden bowl"></div>
    <span class="fav"><svg width="8" height="7" viewBox="0 0 11 10"><path d="M5.5 9.5L1 5a2.6 2.6 0 0 1 4.5-3.2A2.6 2.6 0 0 1 10 5z" fill="#fff"/></svg></span>
  </article>
  <article class="abs product" style="left:145px;top:510px">
    <div class="photo photo--wood" role="img" aria-label="Dried rose petals in a wooden bowl"></div>
    <span class="fav"><svg width="8" height="7" viewBox="0 0 11 10"><path d="M5.5 9.5L1 5a2.6 2.6 0 0 1 4.5-3.2A2.6 2.6 0 0 1 10 5z" fill="#fff"/></svg></span>
  </article>

  <nav class="abs tabbar">
    <div class="tab" style="left:38px"><div class="ic"><svg width="14" height="14" viewBox="0 0 14 14"><path d="M7 1l6 5v7H9V9H5v4H1V6z" fill="#ddd"/></svg></div><span>HOME</span></div>
    <div class="tab" style="left:90px"><div class="ic"><svg width="13" height="14" viewBox="0 0 13 14"><rect x="1" y="2.5" width="11" height="10.5" rx="1" fill="none" stroke="#ddd" stroke-width="1.3"/><path d="M1 5.5h11M4 1v3M9 1v3M4 9l2 2 3-3.5" stroke="#ddd" fill="none" stroke-width="1.3"/></svg></div><span>BOOK</span></div>
    <div class="tab" style="left:142px"><div class="ic"><svg width="14" height="14" viewBox="0 0 14 14"><path d="M1 1h12v9H4l-3 3z" fill="#ddd"/><path d="M3.5 4h7M3.5 6.5h7" stroke="#111" stroke-width="1"/></svg></div><span>CHAT</span></div>
    <div class="tab tab--active" style="left:195px"><div class="ic"><svg width="14" height="14" viewBox="0 0 14 14"><path d="M0.5 1h2l2 7.5h7l1.5-5.5H3.5" fill="none" stroke="#111" stroke-width="1.3"/><path d="M3.7 3h9.3l-1.5 5.5h-7z" fill="#111"/><circle cx="5" cy="12" r="1.2" fill="#111"/><circle cx="11" cy="12" r="1.2" fill="#111"/></svg></div><span>STORE</span></div>
    <div class="tab" style="left:245px"><div class="ic"><svg width="12" height="13" viewBox="0 0 12 13"><circle cx="6" cy="3.5" r="3" fill="#ddd"/><path d="M0 13c0-4 2.5-5.5 6-5.5S12 9 12 13z" fill="#ddd"/></svg></div><span>PROFILE</span></div>
  </nav>
</section>

</body>
</html>
```